Roof Plumbing Company needs simple, modern business card using the attached logo and below details:

Dean Halloway
Summit Gutters Pty Ltd
ABN: 58 214 937 062
Phone: 0417 286 531
Email: summitgutters@mailbrook.com
Website: summitgutters.com.au

For all of your metal roof plumbing requirements contact Summit Gutters for an obligation free quote - no job too big or to small!

Industry/Entity Type

Business

Contact Information for Business Card

Dean Halloway
Summit Gutters Pty Ltd
ABN 58 214 937 062
0417 286 531
summitgutters@mailbrook.com
summitgutters.com.au

Requirements
Must have
• Bright eye catching design, professional look

```html
<!DOCTYPE html>
<html lang="en">
<head>
<meta charset="utf-8">
<title>Summit Gutters – Business Card</title>
<link rel="stylesheet" href="https://fonts.googleapis.com/css2?family=Montserrat:wght@500;600;700&family=Open+Sans:wght@400;600&display=swap">
<style>
  :root {
    --bg: #e4e4e4;
    --card-dark: #3b3b3b;
    --card-dark-hi: #5a5a5a;
    --brand-red: #e3211f;
    --white: #ffffff;
    --ink: #333333;
    --muted: #6b6b6b;
  }
  * { margin: 0; padding: 0; box-sizing: border-box; }
  html, body { width: 1200px; height: 1200px; overflow: hidden; }
  body {
    background: var(--bg);
    font-family: "Open Sans", Arial, sans-serif;
    position: relative;
  }
  .card {
    position: absolute;
    left: 250px;
    width: 700px;
    height: 400px;
    border-radius: 26px;
    overflow: hidden;
    box-shadow: 0 8px 24px rgba(0,0,0,0.18);
  }
  .card--front { top: 150px; }
  .card--back { top: 650px; }

  .dark-surface {
    background: linear-gradient(115deg, var(--card-dark) 0%, var(--card-dark-hi) 45%, var(--card-dark) 100%);
  }

  .brand-name {
    position: absolute;
    display: flex;
    align-items: center;
    gap: 14px;
    font-family: "Montserrat", Arial, sans-serif;
    font-weight: 700;
    color: var(--brand-red);
    text-transform: uppercase;
    line-height: 1.05;
    white-space: nowrap;
  }
  .brand-name__mark {
    width: 22px; height: 22px;
    background: var(--brand-red);
    flex: none;
  }
  .brand-name__line { display: block; }
  .brand-name__sub {
    display: block;
    font-size: 0.45em;
    letter-spacing: 6px;
    margin-top: 8px;
  }
  .card--front .brand-name {
    left: 50%; top: 50%;
    transform: translate(-50%, -50%);
    font-size: 44px;
    letter-spacing: 2px;
  }

  .back-shape { position: absolute; inset: 0; width: 700px; height: 400px; }
  .card--back .brand-name {
    left: 70px; top: 50%;
    transform: translateY(-50%);
    font-size: 30px;
    letter-spacing: 1.5px;
    gap: 12px;
  }
  .card--back .brand-name__mark { width: 16px; height: 16px; }
  .card--back .brand-name__sub { letter-spacing: 4px; margin-top: 6px; }

  .contact {
    position: absolute;
    left: 390px;
    top: 95px;
    color: var(--ink);
  }
  .contact__name {
    font-family: "Montserrat", Arial, sans-serif;
    font-weight: 600;
    font-size: 30px;
    color: var(--brand-red);
  }
  .contact__role {
    font-size: 14px;
    color: var(--muted);
    margin-top: 2px;
    margin-left: 18px;
  }
  .contact__list {
    list-style: none;
    margin-top: 22px;
    font-size: 15.5px;
    line-height: 25px;
  }
  .contact__list li { display: flex; align-items: center; gap: 12px; }
  .contact__icon { width: 15px; height: 15px; flex: none; }
  .contact__abn { padding-left: 27px; }
</style>
</head>
<body>

  <section class="card card--front dark-surface" aria-label="Business card front">
    <div class="brand-name">
      <span class="brand-name__mark"></span>
      <span>
        <span class="brand-name__line">Summit</span>
        <span class="brand-name__line">Gutters</span>
        <span class="brand-name__sub">Pty Ltd</span>
      </span>
    </div>
  </section>

  <section class="card card--back" aria-label="Business card back">
    <svg class="back-shape" viewBox="0 0 700 400" aria-hidden="true">
      <defs>
        <linearGradient id="darkFill" x1="0" y1="0" x2="1" y2="1">
          <stop offset="0" stop-color="#3b3b3b"/>
          <stop offset="0.45" stop-color="#5a5a5a"/>
          <stop offset="1" stop-color="#3b3b3b"/>
        </linearGradient>
      </defs>
      <rect width="700" height="400" fill="url(#darkFill)"/>
      <path d="M200 0 C 260 60, 320 110, 325 220 C 330 320, 335 370, 345 400 L 700 400 L 700 0 Z" fill="var(--brand-red)"/>
      <path d="M212 0 C 272 60, 330 110, 336 220 C 342 320, 347 370, 357 400 L 700 400 L 700 0 Z" fill="var(--white)"/>
    </svg>

    <div class="brand-name">
      <span class="brand-name__mark"></span>
      <span>
        <span class="brand-name__line">Summit</span>
        <span class="brand-name__line">Gutters</span>
        <span class="brand-name__sub">Pty Ltd</span>
      </span>
    </div>

    <div class="contact">
      <h1 class="contact__name">Dean Halloway</h1>
      <p class="contact__role">Director</p>
      <ul class="contact__list">
        <li>
          <svg class="contact__icon" viewBox="0 0 16 16"><path fill="#e3211f" d="M3 2h3l1.5 3.5-2 1.2a8 8 0 0 0 3.8 3.8l1.2-2L14 10v3a1 1 0 0 1-1 1A11 11 0 0 1 2 3a1 1 0 0 1 1-1z"/></svg>
          0417 286 531
        </li>
        <li>
          <svg class="contact__icon" viewBox="0 0 16 16"><circle cx="8" cy="8" r="6.5" fill="none" stroke="#e3211f" stroke-width="1.6"/><path d="M1.5 8h13M8 1.5c-3 3.5-3 9.5 0 13M8 1.5c3 3.5 3 9.5 0 13" fill="none" stroke="#e3211f" stroke-width="1.2"/></svg>
          summitgutters.com.au
        </li>
        <li>
          <svg class="contact__icon" viewBox="0 0 16 16"><rect x="1" y="3" width="14" height="10" rx="1" fill="#e3211f"/><path d="M1.5 3.5 8 9l6.5-5.5" fill="none" stroke="#fff" stroke-width="1.2"/></svg>
          summitgutters@mailbrook.com
        </li>
        <li class="contact__abn">ABN 58 214 937 062</li>
      </ul>
    </div>
  </section>

</body>
</html>
```